Wholesale in Gold Jewellery & Gold Bullion

We are an established gold jewellery and gold bullion wholesaler selling these products to international clients. We already have a name and logo of our company, hence please view attached current card design. We need a completely new design to compliment our business and industry and the final design should be new and elegant.

Contact Information for Business Card

New card details must be same as per current card. Like logo, name, tel no. & etc.

Colors

Designer to choose colors to be used in the design.

```html
<!DOCTYPE html>
<html lang="en">
<head>
<meta charset="utf-8">
<title>Arven &amp; Co Pte Ltd — Business Card</title>
<link rel="stylesheet" href="https://fonts.googleapis.com/css2?family=Cormorant+Garamond:wght@600&family=Ubuntu:wght@400;500;700&display=swap">
<style>
  :root {
    --canvas: #eeeeef;
    --ice: #d0e6f3;
    --ink: #050505;
    --charcoal: #2d2d2f;
    --white: #ffffff;
    --card-shadow: 0 6px 18px rgba(0,0,0,0.18);
  }
  * { box-sizing: border-box; margin: 0; padding: 0; }
  html, body {
    width: 1200px; height: 1176px; overflow: hidden;
    background: var(--canvas);
  }
  .canvas { position: relative; width: 1200px; height: 1176px; }

  .card {
    position: absolute; width: 560px; height: 320px;
    box-shadow: var(--card-shadow); overflow: hidden;
  }

  /* Front */
  .card--front {
    left: 90px; top: 160px; background: var(--ice);
    display: flex; flex-direction: column; align-items: center; justify-content: center; gap: 22px;
  }
  .brand { display: flex; align-items: center; gap: 16px; }
  .brand__dot { width: 22px; height: 22px; border-radius: 50%; background: var(--charcoal); }
  .brand__name {
    font-family: "Cormorant Garamond", serif; font-weight: 600;
    color: var(--charcoal); font-size: 34px; letter-spacing: 1px;
  }

  /* Back */
  .card--back { left: 550px; top: 640px; background: var(--ice); }
  .card__shape { position: absolute; inset: 0; }
  .back-brand {
    position: absolute; right: 34px; top: 38px;
    display: flex; align-items: center; gap: 10px;
  }
  .back-brand .brand__dot { width: 16px; height: 16px; background: var(--ink); }
  .back-brand .brand__name { font-size: 24px; color: var(--ink); }

  .person { position: absolute; left: 38px; top: 128px; color: var(--white); font-family: "Ubuntu", sans-serif; }
  .person__name { font-size: 21px; font-weight: 700; color: var(--ice); }
  .person__role { font-size: 14px; font-weight: 500; color: var(--ice); margin-top: 2px; }

  .contacts {
    position: absolute; left: 38px; top: 214px; list-style: none;
    font-family: "Ubuntu", sans-serif; font-size: 15px; font-weight: 500; color: var(--white);
  }
  .contacts li { display: flex; align-items: center; gap: 10px; height: 22px; }
  .contacts svg { width: 15px; height: 15px; flex: none; }

  .address {
    position: absolute; left: 300px; top: 138px;
    font-family: "Ubuntu", sans-serif; font-size: 15px; font-weight: 500;
    color: var(--white); line-height: 1.45;
    display: flex; gap: 10px; align-items: flex-start;
  }
  .address svg { width: 14px; height: 18px; margin-top: 1px; flex: none; }
</style>
</head>
<body>
<main class="canvas">

  <section class="card card--front" aria-label="Business card front">
    <div class="brand">
      <span class="brand__dot"></span>
      <span class="brand__name">ARVEN &amp; CO PTE LTD</span>
    </div>
  </section>

  <section class="card card--back" aria-label="Business card back">
    <svg class="card__shape" viewBox="0 0 560 320" preserveAspectRatio="none" aria-hidden="true">
      <polygon points="0,50 180,50 560,150 560,320 0,320" fill="var(--ink)"/>
      <line x1="118" y1="122" x2="300" y2="68" stroke="var(--ice)" stroke-width="4"/>
      <line x1="40" y1="202" x2="260" y2="202" stroke="var(--ice)" stroke-width="4"/>
    </svg>

    <div class="back-brand">
      <span class="brand__dot"></span>
      <span class="brand__name">ARVEN &amp; CO</span>
    </div>

    <div class="person">
      <p class="person__name">Rohan Vidyakar</p>
      <p class="person__role">Director</p>
    </div>

    <ul class="contacts">
      <li>
        <svg viewBox="0 0 16 16"><rect x="4" y="1" width="8" height="14" rx="1.5" fill="none" stroke="var(--white)" stroke-width="1.4"/><circle cx="8" cy="12.5" r="0.9" fill="var(--white)"/></svg>
        <span>+65 6104 2800</span>
      </li>
      <li>
        <svg viewBox="0 0 16 16"><path d="M3 1.5l3 .5 1 3.5-2 1.5a9 9 0 0 0 4.5 4.5l1.5-2 3.5 1 .5 3c-7 1.5-13.5-5-12-12z" fill="var(--white)"/></svg>
        <span>+65 6158 2047</span>
      </li>
      <li>
        <svg viewBox="0 0 16 16"><rect x="1.5" y="6" width="13" height="8" rx="1" fill="none" stroke="var(--white)" stroke-width="1.3"/><path d="M3 6c0-3 10-3 10 0" fill="none" stroke="var(--white)" stroke-width="1.3"/><circle cx="8" cy="10" r="1.6" fill="var(--white)"/></svg>
        <span>+65 9032 5516</span>
      </li>
      <li>
        <svg viewBox="0 0 16 16"><rect x="1" y="3" width="14" height="10" rx="1" fill="var(--white)"/><path d="M1.5 3.5L8 9l6.5-5.5" fill="none" stroke="var(--ink)" stroke-width="1.3"/></svg>
        <span>rohan@arvenco.com</span>
      </li>
    </ul>

    <div class="address">
      <svg viewBox="0 0 14 18"><path d="M7 1a6 6 0 0 0-6 6c0 4.5 6 10 6 10s6-5.5 6-10a6 6 0 0 0-6-6z" fill="var(--white)"/><circle cx="7" cy="7" r="2.3" fill="var(--ink)"/></svg>
      <p>52 Linden Quay Road,<br>Singapore 318204.</p>
    </div>
  </section>

</main>
</body>
</html>
```